Varemo Group Business Card Design

The CEO is looking for a new trendy look for his business card.
You can stay with current branding or come up with something new/creative. It can be 3D, including Medical Office buildings. You can use our logo in a variety of colors. Please include name, title, company name, company website, email address, cell number

Target Market(s)

Real Estate Development and Construction

Industry/Entity Type

Health care real estate

Contact Information for Business Card

Rohesh Kumbar, CEO M-727.418.9062 E-roheshkumbar@varemo.com Address:4100 Lindell Ave, Tampa, FL 33611 www.varemo.com

Font styles to use
Other font styles liked:
• Be creative

Requirements
Must have
• Creative, trendy look
Nice to have
• Please go to our website to get a feel- www. varemo.com
Should not have
• small fonts

```html
<!DOCTYPE html>
<html lang="en">
<head>
<meta charset="utf-8">
<title>Varemo Group Business Card</title>
<link rel="stylesheet" href="https://fonts.googleapis.com/css2?family=Poppins:wght@400;700&display=swap">
<style>
  :root {
    --page-bg: #e6e6e8;
    --card-white: #ffffff;
    --brand-red: #a01a24;
    --ink: #1d1d1f;
    --rule: #3c4a66;
    --photo-sky: #b8c4da;
    --photo-wall: #d9dbe6;
    --photo-green: #3f5a2e;
    --photo-road: #3a3d45;
  }
  * { box-sizing: border-box; margin: 0; padding: 0; }
  html, body {
    width: 1200px; height: 900px; overflow: hidden;
    background: var(--page-bg);
    font-family: "Poppins", sans-serif;
  }
  .canvas { position: relative; width: 1200px; height: 900px; }
  .card {
    position: absolute; left: 250px; width: 700px; height: 400px;
    border-radius: 28px; overflow: hidden;
    box-shadow: 0 10px 30px rgba(0,0,0,.18);
  }
  .card--front { top: 40px; }
  .card--back { top: 460px; background: var(--card-white); }

  .front-photo {
    position: absolute; inset: 0;
    background: linear-gradient(180deg, var(--photo-sky) 0%, var(--photo-wall) 38%, #c3c6d3 60%, var(--photo-green) 80%, var(--photo-road) 100%);
  }
  .front-wordmark {
    position: absolute; top: 48px; left: 0; right: 0; text-align: center;
    font-weight: 700; font-size: 62px; letter-spacing: -1px; line-height: 1.2;
    color: var(--ink);
  }

  .back-wordmark {
    position: absolute; top: 36px; right: 50px;
    font-weight: 700; font-size: 56px; letter-spacing: -1px; line-height: 1.2;
    color: var(--brand-red);
  }
  .back-block {
    position: absolute; left: 0; top: 165px; width: 230px; height: 145px;
    background: var(--brand-red);
  }
  .holder { position: absolute; left: 44px; top: 314px; }
  .holder-name {
    font-weight: 700; font-size: 20px; color: var(--brand-red);
    text-transform: uppercase; line-height: 1.2;
  }
  .holder-role { font-size: 15px; line-height: 1.4; color: var(--ink); }
  .sep { color: var(--brand-red); padding: 0 4px; }
  .contact-rule {
    position: absolute; left: 44px; right: 40px; top: 364px;
    height: 1px; background: var(--rule);
  }
  .contact-line {
    position: absolute; left: 44px; top: 369px;
    font-size: 13px; line-height: 1.5; color: var(--ink); white-space: nowrap;
  }
</style>
</head>
<body>
<div class="canvas">
  <section class="card card--front">
    <div class="front-photo" role="img" aria-label="Rendered view of modern medical office buildings around a landscaped courtyard under a pale sky"></div>
    <div class="front-wordmark">Varemo Group</div>
  </section>

  <section class="card card--back">
    <div class="back-wordmark">Varemo Group</div>
    <div class="back-block"></div>
    <div class="holder">
      <p class="holder-name">Rohesh Kumbar</p>
      <p class="holder-role">CEO<span class="sep">|</span>T. 727.418.9062</p>
    </div>
    <div class="contact-rule"></div>
    <p class="contact-line">4100 Lindell Ave, Tampa, FL 33611<span class="sep">|</span>roheshkumbar@varemo.com<span class="sep">|</span>www.varemo.com</p>
  </section>
</div>
</body>
</html>
```